KVT Social Media Graphics (Square)

Use the following images and headlines to create 7 individual social media graphics (square size); You can mix and match the text that's there to create different social media graphics. Note: each graphic should have one of the pictures of the bottle on it and/or one of the images with a person on it (pics attached to the brief)

Target Market(s)

women and men who are overweight looking for fast, healthy weight loss

Industry/Entity Type

health and wellness

Colors
0054AA
0677BA
7BADD7
CADEEF
E8F1F8

Requirements
Must have
• Use color scheme that's complimentary to the blood sugar bottle
Nice to have
• the text provided in the WORD document

```html
<!DOCTYPE html>
<html lang="en">
<head>
<meta charset="utf-8">
<title>KVT Formula – Lose Weight Without the Side Effects</title>
<link href="https://fonts.googleapis.com/css2?family=Plus+Jakarta+Sans:wght@600;800&display=swap" rel="stylesheet">
<style>
  :root {
    --headline-blue: #0f40cc;
    --accent-yellow: #ffb800;
    --band-blue-top: #1a5cff;
    --band-blue-bottom: #3a33ff;
    --sky-light: #ffffff;
    --sky-mid: #f0f0f0;
    --sky-gray: #d8d8d8;
    --pill-bg: #d6d6e4;
    --pill-text: #1a44cc;
    --bottle-white: #f4f5f8;
    --bottle-navy: #3b3f8f;
  }
  html, body {
    margin: 0;
    padding: 0;
    width: 1200px;
    height: 1200px;
    overflow: hidden;
  }
  .social-graphic {
    position: relative;
    width: 1200px;
    height: 1200px;
    overflow: hidden;
    font-family: "Plus Jakarta Sans", sans-serif;
    background: radial-gradient(ellipse 80% 70% at 50% 28%, var(--sky-light) 0%, var(--sky-mid) 50%, var(--sky-gray) 100%);
  }
  .blue-band {
    position: absolute;
    inset: 0;
    width: 1200px;
    height: 1200px;
  }
  .headline {
    position: absolute;
    margin: 0;
    color: var(--headline-blue);
    font-weight: 800;
    line-height: 1;
    white-space: nowrap;
    z-index: 3;
  }
  .headline-lose {
    left: 132px;
    top: 98px;
    font-size: 88px;
    letter-spacing: -2px;
  }
  .headline-without {
    left: 212px;
    top: 210px;
    font-size: 106px;
    letter-spacing: -3px;
  }
  .headline-effects {
    left: 212px;
    top: 295px;
    font-size: 152px;
    letter-spacing: -5px;
  }
  .accent-rule {
    position: absolute;
    left: 178px;
    top: 205px;
    width: 3px;
    height: 236px;
    background: var(--accent-yellow);
    z-index: 3;
  }
  .product-bottle {
    position: absolute;
    border-radius: 40px 40px 28px 28px;
    background: linear-gradient(180deg, #c9cbd2 0%, var(--bottle-white) 22%, var(--bottle-white) 62%, var(--bottle-navy) 78%, #4a5bd0 100%);
    box-shadow: 0 20px 30px rgba(0,0,40,0.25);
  }
  .bottle-left { left: 193px; top: 584px; width: 223px; height: 478px; }
  .bottle-right { left: 779px; top: 584px; width: 215px; height: 478px; }
  .bottle-center { left: 415px; top: 440px; width: 364px; height: 690px; z-index: 2; }
  .info-pill {
    position: absolute;
    height: 32px;
    border-radius: 16px;
    background: var(--pill-bg);
    color: var(--pill-text);
    font-weight: 600;
    font-size: 22px;
    line-height: 32px;
    text-align: center;
    white-space: nowrap;
  }
  .pill-capsules { left: 96px; top: 1094px; width: 289px; }
  .pill-supplement { left: 818px; top: 1092px; width: 238px; }
</style>
</head>
<body>
  <main class="social-graphic">
    <svg class="blue-band" viewBox="0 0 1200 1200" aria-hidden="true">
      <defs>
        <linearGradient id="bandFill" x1="0" y1="0" x2="0" y2="1">
          <stop offset="0" stop-color="#1a5cff"/>
          <stop offset="1" stop-color="#3a33ff"/>
        </linearGradient>
      </defs>
      <path d="M0,621 Q600,1180 1200,602 L1200,1200 L0,1200 Z" fill="url(#bandFill)"/>
      <path d="M0,621 Q600,1180 1200,602" fill="none" stroke="#ffb800" stroke-width="10"/>
    </svg>

    <h1 class="headline headline-lose">Lose Weight,</h1>
    <div class="accent-rule"></div>
    <p class="headline headline-without">Without the</p>
    <p class="headline headline-effects">Side Effects</p>

    <div class="product-bottle bottle-left" role="img" aria-label="KVT Formula supplement bottle, 60 vegetable capsules"></div>
    <div class="product-bottle bottle-right" role="img" aria-label="KVT Formula supplement bottle, 60 vegetable capsules"></div>
    <div class="product-bottle bottle-center" role="img" aria-label="KVT Formula supplement bottle, front view with label listing blood sugar and weight support"></div>

    <div class="info-pill pill-capsules">60 Vegetable Capsules</div>
    <div class="info-pill pill-supplement">Dietary Supplement</div>
  </main>
</body>
</html>
```